Classy, Elegant, Simple Business Card Design

Looking to have a classy, simple, and elegant design. Want a top notch designed business card. I really like the look of the new brivo credit card. I also like the design I attached. I am trying to reach 21-29 year old females for booking us for there wedding or event. We offer Disc Jockey Service, Photo Booth Rentals, and Uplighting .

Target Market(s)

21-28 year old females

Contact Information for Business Card

Has to have logo, website, email, and phone number

Font styles to use
Other font styles liked:
• open to font choice, modern, clean
Designer to choose
33a6d7
0791cd
0555a3
ffffff

Requirements
Must have
• Has to have logo, website, email, and phone number
Nice to have
• I really like the design of the new brivo credit card. I also included my logo and some designs I like
Should not have
• clutter or too much info

```html
<!DOCTYPE html>
<html lang="en">
<head>
<meta charset="utf-8">
<title>Tidewell Event Group – Business Card</title>
<link rel="stylesheet" href="https://fonts.googleapis.com/css2?family=Jost:wght@300;400;600;700&display=swap">
<style>
  :root {
    --bg: #ececec;
    --card: #ffffff;
    --navy: #1d3a66;
    --blue: #0791cd;
    --mid-blue: #0555a3;
    --sky: #33a6d7;
    --grey: #8a8f96;
    --shadow: 0 18px 40px rgba(0, 0, 0, 0.12);
  }
  * { box-sizing: border-box; margin: 0; padding: 0; }
  html, body {
    width: 1200px;
    height: 1200px;
    overflow: hidden;
    background: var(--bg);
    font-family: "Jost", sans-serif;
  }
  .canvas {
    width: 1200px;
    height: 1200px;
    display: flex;
    flex-direction: column;
    align-items: center;
    justify-content: center;
    gap: 90px;
  }
  .card {
    width: 700px;
    height: 400px;
    background: var(--card);
    box-shadow: var(--shadow);
    position: relative;
    overflow: hidden;
  }

  /* Front */
  .card-front .brand {
    position: absolute;
    top: 90px;
    left: 0;
    right: 0;
    text-align: center;
  }
  .brand-name {
    font-size: 46px;
    font-weight: 400;
    letter-spacing: 3px;
    color: var(--mid-blue);
    line-height: 1;
  }
  .brand-sub {
    margin-top: 8px;
    font-size: 15px;
    font-weight: 300;
    letter-spacing: 9px;
    color: var(--grey);
  }
  .front-band {
    position: absolute;
    left: -10px;
    right: -10px;
    bottom: -48px;
    font-size: 150px;
    font-weight: 700;
    line-height: 1;
    letter-spacing: 4px;
    color: var(--blue);
    text-align: center;
    white-space: nowrap;
  }

  /* Back */
  .card-back .brand {
    position: absolute;
    top: 52px;
    left: 56px;
  }
  .card-back .brand-name { font-size: 34px; }
  .card-back .brand-sub { font-size: 11px; letter-spacing: 6px; margin-top: 6px; }
  .contact-list {
    position: absolute;
    top: 190px;
    left: 56px;
    list-style: none;
    display: flex;
    flex-direction: column;
    gap: 12px;
  }
  .contact-item {
    display: flex;
    align-items: center;
    gap: 14px;
    font-size: 15px;
    font-weight: 600;
    color: var(--mid-blue);
  }
  .contact-item svg { width: 16px; height: 16px; flex: none; }
  .holder {
    position: absolute;
    right: 64px;
    bottom: 60px;
    text-align: left;
  }
  .holder-name {
    font-size: 38px;
    font-weight: 700;
    color: var(--blue);
    line-height: 1;
  }
  .holder-role {
    margin-top: 4px;
    font-size: 15px;
    font-weight: 600;
    color: var(--mid-blue);
  }
</style>
</head>
<body>
<main class="canvas">
  <section class="card card-front">
    <div class="brand">
      <p class="brand-name">TIDEWELL</p>
      <p class="brand-sub">EVENT GROUP</p>
    </div>
    <p class="front-band">TIDEWELL</p>
  </section>

  <section class="card card-back">
    <div class="brand">
      <p class="brand-name">TIDEWELL</p>
      <p class="brand-sub">EVENT GROUP</p>
    </div>
    <ul class="contact-list">
      <li class="contact-item">
        <svg viewBox="0 0 16 16" aria-hidden="true"><path d="M4 1.5h2.5l1 3.5-1.7 1.2a8 8 0 0 0 4 4L11 8.5l3.5 1V12a2 2 0 0 1-2 2A11 11 0 0 1 2 3.5a2 2 0 0 1 2-2z" fill="var(--sky)"/></svg>
        76xxxxxxx
      </li>
      <li class="contact-item">
        <svg viewBox="0 0 16 16" aria-hidden="true"><rect x="4" y="1" width="8" height="14" rx="1.5" fill="var(--sky)"/><rect x="5.5" y="3" width="5" height="8" fill="#fff"/></svg>
        76xxxxxxx
      </li>
      <li class="contact-item">
        <svg viewBox="0 0 16 16" aria-hidden="true"><rect x="1" y="3" width="14" height="10" rx="1" fill="var(--sky)"/><path d="M1.5 3.8 8 9l6.5-5.2" fill="none" stroke="#fff" stroke-width="1.4"/></svg>
        hello@tidewell.com
      </li>
      <li class="contact-item">
        <svg viewBox="0 0 16 16" aria-hidden="true"><circle cx="8" cy="8" r="6.5" fill="none" stroke="var(--sky)" stroke-width="1.6"/><path d="M1.5 8h13M8 1.5c-3 3.5-3 9.5 0 13M8 1.5c3 3.5 3 9.5 0 13" fill="none" stroke="var(--sky)" stroke-width="1.2"/></svg>
        www.tidewell.com
      </li>
    </ul>
    <div class="holder">
      <p class="holder-name">Marco</p>
      <p class="holder-role">Photographer</p>
    </div>
  </section>
</main>
</body>
</html>
```